Keys to a Successful Retirement

We have an audience of 175 who will be viewing these slides. They are designed to be "visual aids" to the presentation -- not a hand out. I am uploading the power point that I did --- we want a professional look but want to keep the words on the slides as they are. We want to keep the civic ledger logo we pasted and the Brantford logo, (our firm). Other than that, feel free to swap out pictures if you have better ones. We want to remain in Power Point so that we can edit it as necessary and display using our existing computers.

```html
<!DOCTYPE html>
<html lang="en">
<head>
<meta charset="utf-8">
<title>Keys to a Successful Retirement</title>
<link rel="stylesheet" href="https://fonts.googleapis.com/css2?family=PT+Sans+Narrow:wght@400;700&family=PT+Sans:ital@1&display=swap">
<style>
  :root {
    --navy: #0e3f78;
    --navy-deep: #061d3d;
    --bar-top: #1d4f8c;
    --ink: #1d2a3a;
    --tick: #3aa55a;
    --bg-center: #f3fbfd;
    --bg-edge: #cfe9f2;
    --brand: #8d9aa8;
    --btn: #18212c;
  }
  * { margin: 0; padding: 0; box-sizing: border-box; }
  html, body { width: 1200px; height: 900px; overflow: hidden; }
  body { font-family: "PT Sans Narrow", "Arial Narrow", sans-serif; }
  .slide {
    position: relative; width: 1200px; height: 900px; overflow: hidden;
    background: radial-gradient(ellipse at 45% 45%, var(--bg-center) 0%, #e4f4f9 55%, var(--bg-edge) 100%);
  }
  .ribbon { position: absolute; left: 0; top: 30px; }
  .slide-title {
    position: absolute; left: 60px; top: 28px;
    font-weight: 700; font-size: 48px; color: var(--navy); letter-spacing: -0.5px;
  }
  .section-heading {
    position: absolute; left: 88px; top: 144px;
    font-weight: 700; font-size: 35px; color: var(--navy); letter-spacing: -0.3px;
  }
  .checklist {
    position: absolute; left: 92px; top: 205px; width: 1000px; list-style: none;
    font-size: 24px; line-height: 39px; color: var(--ink);
  }
  .checklist li { position: relative; padding-left: 43px; }
  .checklist .check { position: absolute; left: 0; top: 8px; width: 28px; height: 26px; }
  .brand-name {
    position: absolute; right: 32px; top: 684px;
    font-weight: 400; font-size: 44px; color: var(--brand); letter-spacing: 1px;
  }
  .footer-bar {
    position: absolute; left: 0; bottom: 0; width: 1200px; height: 90px;
    background: linear-gradient(to bottom, var(--bar-top) 0%, #0d305f 45%, var(--navy-deep) 100%);
    border-top: 3px solid #2a2f36;
  }
  .page-number {
    position: absolute; left: 33px; top: 18px; width: 57px; height: 51px;
    background: var(--btn); border: 2px solid #6d7a88; border-radius: 4px;
    color: #fff; font-family: "PT Sans", sans-serif; font-size: 30px;
    display: flex; align-items: center; justify-content: center;
  }
  .tagline {
    position: absolute; left: 129px; top: 27px;
    font-family: "PT Sans", sans-serif; font-style: italic; font-size: 26px; color: #fff;
  }
  .nav-button { position: absolute; top: 16px; width: 110px; height: 58px; }
  .nav-button text { font-family: "PT Sans", sans-serif; font-size: 23px; fill: #fff; }
  .nav-back { left: 955px; }
  .nav-next { left: 1070px; }
</style>
</head>
<body>
<div class="slide">
  <svg width="0" height="0" style="position:absolute">
    <defs>
      <symbol id="check" viewBox="0 0 28 26">
        <rect x="1.5" y="5.5" width="19" height="19" fill="none" stroke="#13385f" stroke-width="2.5"/>
        <path d="M5 14 L11 20 L26 2" fill="none" stroke="var(--tick)" stroke-width="4" stroke-linecap="round" stroke-linejoin="round"/>
      </symbol>
    </defs>
  </svg>

  <svg class="ribbon" width="46" height="58" viewBox="0 0 46 58">
    <path d="M0 0 H30 L46 29 L30 58 H0 Z" fill="#0e3f78"/>
    <path d="M0 0 H30 L46 29 H0 Z" fill="#1c5799"/>
  </svg>
  <h1 class="slide-title">Keys to a Successful Retirement</h1>

  <h2 class="section-heading">Planning Ahead With Confidence</h2>

  <ul class="checklist">
    <li><svg class="check"><use href="#check"/></svg>Start saving early and let compound growth work for you</li>
    <li><svg class="check"><use href="#check"/></svg>Set clear retirement goals for lifestyle, travel and family</li>
    <li><svg class="check"><use href="#check"/></svg>Build a realistic budget for the years after your final paycheck</li>
    <li><svg class="check"><use href="#check"/></svg>“Save Early and Save Often” approach to building wealth</li>
    <li><svg class="check"><use href="#check"/></svg>Understand your civic ledger benefits and the best age to begin claiming them</li>
    <li><svg class="check"><use href="#check"/></svg>Make the most of employer plans and matching contributions</li>
    <li><svg class="check"><use href="#check"/></svg>Diversify, rebalance, and review investments every year</li>
    <li><svg class="check"><use href="#check"/></svg>Plan for healthcare costs, long-term care, and the rising cost of living so that<br>your savings last as long as you do, all while keeping enough flexibility to enjoy<br>the retirement you have worked for</li>
    <li><svg class="check"><use href="#check"/></svg>Protect your estate with updated wills, beneficiaries and insurance</li>
    <li><svg class="check"><use href="#check"/></svg>Not Just a Number! Retirement is a plan for the life<br>you want to live, year after year.</li>
  </ul>

  <div class="brand-name">Brantford Financial Group</div>

  <footer class="footer-bar">
    <div class="page-number">03</div>
    <p class="tagline">Guiding your path to a confident retirement</p>
    <svg class="nav-button nav-back" viewBox="0 0 110 58">
      <path d="M22 2 H104 Q108 2 108 6 V52 Q108 56 104 56 H22 L2 29 Z" fill="#18212c" stroke="#6d7a88" stroke-width="2"/>
      <text x="60" y="37" text-anchor="middle">Back</text>
    </svg>
    <svg class="nav-button nav-next" viewBox="0 0 110 58">
      <path d="M6 2 H88 L108 29 L88 56 H6 Q2 56 2 52 V6 Q2 2 6 2 Z" fill="#18212c" stroke="#6d7a88" stroke-width="2"/>
      <text x="50" y="37" text-anchor="middle">Next</text>
    </svg>
  </footer>
</div>
</body>
</html>
```